QUICK: Fresh Ideas for New Home Page Design!

Simply improve on our home page design and provide PSD file.

We are Brightpath Coverage, a trusted health insurance comparison site to make shopping and enrolling in Plumwell easy. We are certified agents for Sheltered Pacifica, the state's health insurance marketplace (logo attached).

Use flat UI colors.

Looking for a fun design. Reference websites are:
www.vantrelo.example
www.qubimar.example
www.tolvex.example
www.findmyplan.example
www.marvelcoveragehub.example

Target Market(s)

Individuals ages 18 - 64 shopping for health insurance for themselves and/or their family members. California residents. Don't have health insurance and want it or have it and looking to change.

Industry/Entity Type

Shopping

Font styles to use
Sans Serif

Colors
faed22
33a6d7
33b7a4

Requirements
Must have
• No stock photos. No medical or doctor images or photos. Use images of families. Friendly. Modern fonts and flat UI colors.
Nice to have
• Create a mock-up logo for Brightpath Coverage.
Should not have
• No stock looking photos or images

```html
<!DOCTYPE html>
<html lang="en">
<head>
<meta charset="utf-8">
<title>Sheltered Pacifica – Home</title>
<link rel="stylesheet" href="https://fonts.googleapis.com/css2?family=Open+Sans:wght@300;400;600;700&display=swap">
<style>
:root{
  --teal:#2fa9a5;
  --blue:#33a6d7;
  --blue-pale:#dff0f7;
  --ink:#444;
  --bar:#4a4a4a;
  --footer:#333;
  --footer-deep:#282828;
  --white:#fff;
  --line:#e3e3e3;
  --ring:#a9dedb;
}
*{box-sizing:border-box;margin:0;padding:0}
html,body{width:1200px;height:3309px;overflow:hidden}
body{font-family:"Open Sans",Arial,sans-serif;color:var(--ink);background:var(--white);position:relative}
.band{position:absolute;left:0;width:1200px}

/* top utility bar */
.topbar{top:0;height:35px;background:var(--teal);color:var(--white);font-size:12px}
.topbar .tagline{position:absolute;left:172px;top:9px;font-weight:600}
.topbar .util{position:absolute;left:600px;top:6px;display:flex;gap:18px;align-items:center;height:22px}
.topbar .sep{opacity:.6}
.topbar .login{background:#e9e9e9;color:#555;padding:3px 16px;border-radius:2px;font-size:11px}

/* header */
.site-header{top:35px;height:75px;background:var(--white);border-bottom:1px solid var(--line)}
.brand{position:absolute;left:172px;top:9px;display:flex;align-items:center;gap:10px}
.brand .mark{display:block;width:56px;height:56px;border-radius:50%;background:var(--teal)}
.brand .name{font-weight:700;font-size:16px;line-height:18px;color:#2b4a6b}
.nav-link{position:absolute;top:29px;font-size:12.5px;color:#555;white-space:nowrap}

/* hero */
.hero{top:110px;height:453px;background:linear-gradient(180deg,#cfe4ef 0%,#e8eef0 55%,#c9c3b3 100%);overflow:hidden}
.hero .photo{position:absolute;left:560px;top:0;width:560px;height:453px;background:linear-gradient(160deg,#d9c8b5 0%,#b98f73 45%,#c85d3a 100%);opacity:.55}
.hero h1{position:absolute;left:172px;top:122px;font-weight:400;font-size:32px;color:var(--teal);white-space:nowrap}
.hero p{position:absolute;left:172px;top:172px;width:440px;font-size:12px;line-height:21px;color:#333}
.hero .actions{position:absolute;left:172px;top:280px;display:flex;gap:14px}
.hero .arrow{position:absolute;top:170px}
.btn{display:inline-block;background:var(--teal);color:var(--white);font-size:13px;text-align:center;padding:12px 0;width:144px;border-radius:2px;text-transform:uppercase}

/* quick links bar */
.quickbar{top:563px;height:73px;background:var(--bar);color:var(--white);font-size:13px}
.qitem{position:absolute;top:16px;display:flex;align-items:center;gap:14px;white-space:nowrap}
.qitem .ico{display:block;width:40px;height:40px;border-radius:50%;background:var(--teal)}
.qdiv{position:absolute;top:14px;width:1px;height:46px;background:#666}

.section-title{position:absolute;left:0;width:1200px;text-align:center;font-weight:300;font-size:29px;line-height:36px}

/* welcome */
.welcome{top:636px;height:361px}
.welcome .section-title{top:44px;color:var(--teal)}
.welcome .intro{position:absolute;left:220px;top:92px;width:760px;text-align:center;font-size:11.5px;line-height:21px;color:#555}
.stat{position:absolute;top:186px;display:flex;align-items:center;gap:14px}
.stat .num{font-size:29px;color:var(--blue);font-weight:300;line-height:34px}
.stat .cap{font-size:11px;color:#555;line-height:14px}

/* features */
.complicated{top:997px;height:477px;background:linear-gradient(135deg,#5e5852 0%,#8a7a68 45%,#6c6259 100%)}
.complicated .section-title{top:44px;color:var(--white)}
.feature{position:absolute;display:flex;align-items:center;gap:20px;color:var(--white);font-size:14px;line-height:23px}
.feature svg{flex:none}
.complicated .cta{position:absolute;left:510px;top:384px}

/* premiums */
.premiums{top:1474px;height:814px}
.premiums .section-title{top:44px;color:var(--teal)}
.person{position:absolute;width:200px;text-align:center;font-size:14px;color:#555;line-height:24px}
.person .portrait{margin:0 auto 10px;width:154px;height:154px;border-radius:50%;border:8px solid var(--ring)}
.premiums .count{position:absolute;left:0;top:637px;width:1200px;text-align:center;font-size:31px;line-height:40px;color:#333}
.premiums .cta{position:absolute;left:492px;top:704px}

/* testimonials */
.testimonials{top:2288px;height:355px;background:var(--teal)}
.testimonials .section-title{top:38px;color:var(--white)}
.testimonials .portrait{position:absolute;left:219px;top:108px;width:180px;height:180px;border-radius:50%;background:linear-gradient(160deg,#f2dcc4,#d9b48f);border:5px solid #9ed7d3}
.testimonials blockquote{position:absolute;left:457px;top:130px;width:520px;color:var(--white);font-size:12px;line-height:22px;font-style:italic}
.testimonials .who{position:absolute;left:488px;top:242px;color:var(--white);font-size:12.5px}
.testimonials .q{position:absolute;color:var(--white);font-size:40px;font-family:Georgia,serif;line-height:1}
.slide-arrow{position:absolute}

/* partners */
.choices{top:2643px;height:265px}
.choices .section-title{top:50px;color:var(--teal)}
.partner{position:absolute;top:130px;width:148px;height:77px;border:2px solid #ddd;display:flex;align-items:center;justify-content:center;font-size:19px;font-weight:700;color:#2a6aa6}

/* footer */
.site-footer{top:2908px;height:269px;background:var(--footer);color:#ccc;font-size:11px}
.foot-title{position:absolute;top:38px;font-weight:400;font-size:17px;color:var(--teal)}
.foot-list{position:absolute;list-style:none;line-height:22px}
.follow{position:absolute;left:172px;top:160px;display:flex;align-items:center;gap:10px}
.follow .label{color:var(--teal);font-size:14px}
.follow .social{display:block;width:26px;height:26px;border-radius:50%;background:#777}
.news{position:absolute;left:656px;display:flex;gap:14px;width:240px;font-size:11px;line-height:16px}
.news .date{flex:none;width:48px;height:48px;border-radius:50%;background:var(--teal);color:var(--white);font-size:9px;text-align:center;padding-top:6px;line-height:12px}
.news b{color:var(--teal);font-weight:400}

/* chat */
.chat{position:absolute;left:927px;top:2974px;width:265px;height:203px;background:var(--white);border-radius:4px;box-shadow:0 0 6px rgba(0,0,0,.35)}
.chat .brandline{position:absolute;left:24px;top:38px;display:flex;align-items:center;gap:10px;font-size:24px;color:#333}
.chat .dot{display:block;width:38px;height:38px;border-radius:50%;background:var(--teal)}
.chat .input{position:absolute;left:22px;top:120px;width:222px;height:58px;border:1px solid #ccc;font-size:11px;color:#666;padding:8px}
.chat .close{position:absolute;left:246px;top:-8px;width:20px;height:20px;border-radius:50%;background:#999;color:#fff;font-size:12px;text-align:center;line-height:20px}

.legal{top:3177px;height:132px;background:var(--footer-deep);color:#bbb;font-size:10.5px;line-height:19px;text-align:center;padding:26px 250px 0}
.legal .code{position:absolute;left:1136px;top:60px}
</style>
</head>
<body>

<div class="band topbar">
  <div class="tagline">A Sunward Crest Insurance Services Inc. Company</div>
  <div class="util"><span>About Us</span><span class="sep">|</span><span>Resources</span><span class="sep">|</span><span>Contact Us</span><span>&#9742; 800-555-0147</span><span class="login">Account / Login</span></div>
</div>

<header class="band site-header">
  <div class="brand"><span class="mark"></span><span class="name">SHELTERED<br>PACIFICA</span></div>
  <nav>
    <span class="nav-link" style="left:482px">Home</span>
    <span class="nav-link" style="left:565px">Health Plans</span>
    <span class="nav-link" style="left:683px">Health Benefits</span>
    <span class="nav-link" style="left:815px">Affordable Options</span>
    <span class="nav-link" style="left:965px">Employers</span>
  </nav>
</header>

<section class="band hero">
  <div class="photo" role="img" aria-label="Father teaching his young son in a helmet to ride a red bicycle along a beach promenade"></div>
  <svg class="arrow" style="left:72px" width="26" height="70" viewBox="0 0 26 70"><path d="M22 2 L4 35 L22 68" fill="none" stroke="#fff" stroke-width="2"/></svg>
  <svg class="arrow" style="left:1100px" width="26" height="70" viewBox="0 0 26 70"><path d="M4 2 L22 35 L4 68" fill="none" stroke="#fff" stroke-width="2"/></svg>
  <h1>Lorem Ipsum is simply</h1>
  <p>Lorem Ipsum is simply dummy text of the printing and typesetting industry. Lorem Ipsum has been the industry's standard dummy text ever since the 1500s, when an unknown printer took a galley of type and scrambled it to make a type specimen book.</p>
  <div class="actions"><span class="btn">Apply Now</span><span class="btn">Find Plans</span><span class="btn" style="width:150px">Renew Now</span></div>
</section>

<section class="band quickbar">
  <div class="qitem" style="left:174px"><span class="ico"></span>Do I Qualify?</div>
  <div class="qdiv" style="left:353px"></div>
  <div class="qitem" style="left:388px"><span class="ico"></span>Employers</div>
  <div class="qdiv" style="left:555px"></div>
  <div class="qitem" style="left:602px"><span class="ico"></span>Get Help</div>
  <div class="qdiv" style="left:765px"></div>
  <div class="qitem" style="left:815px"><span class="ico"></span>Shop + Compare</div>
</section>

<section class="band welcome">
  <h2 class="section-title">Welcome to Sheltered Pacifica</h2>
  <p class="intro">Consequat id duo, cu aeterno inductum his. Ornatus docendi instructior ex sea. Ei sonet aeterno maiorum ius, natum dolorum invenire mea ex, ne eius suscipiantur duo. Pro quando dictas ad. Dolores urbanitas interesset his teele uewan dashen.</p>
  <div class="stat" style="left:218px">
    <svg width="112" height="112" viewBox="0 0 112 112"><circle cx="56" cy="56" r="54" fill="#dff0f7"/><path d="M56 56 L56 2 A54 54 0 1 1 2 56 Z" fill="#33a6d7"/></svg>
    <div><div class="num">75%</div><div class="cap">Our best Skill</div></div>
  </div>
  <div class="stat" style="left:490px">
    <svg width="112" height="112" viewBox="0 0 112 112"><circle cx="56" cy="56" r="48" fill="none" stroke="#dff0f7" stroke-width="10"/><circle cx="56" cy="56" r="48" fill="none" stroke="#33a6d7" stroke-width="10" stroke-dasharray="181 302" transform="rotate(-90 56 56)"/><text x="56" y="66" text-anchor="middle" font-size="28" fill="#33a6d7" font-family="Open Sans, sans-serif">60%</text></svg>
    <div><div class="num">75%</div><div class="cap">Our best Skill</div></div>
  </div>
  <div class="stat" style="left:776px">
    <svg width="112" height="112" viewBox="0 0 112 112"><circle cx="56" cy="56" r="48" fill="none" stroke="#dff0f7" stroke-width="10"/><circle cx="56" cy="56" r="48" fill="none" stroke="#33a6d7" stroke-width="10" stroke-dasharray="241 302" transform="rotate(-90 56 56)"/><text x="56" y="66" text-anchor="middle" font-size="28" fill="#33a6d7" font-family="Open Sans, sans-serif">60%</text></svg>
    <div><div class="num">75%</div><div class="cap">Our best Skill</div></div>
  </div>
</section>

<section class="band complicated" role="img" aria-label="Background photo of a smiling older couple embracing outdoors, darkened">
  <h2 class="section-title">Health Insurance Doesn't Have To Be Complicated</h2>
  <div class="feature" style="left:192px;top:136px"><svg width="76" height="76" viewBox="0 0 76 76"><circle cx="38" cy="38" r="36" fill="none" stroke="#fff" stroke-width="2"/><path d="M24 50h28M28 48v-8M35 48v-12M42 48v-16M49 48v-20" stroke="#fff" stroke-width="4"/></svg><span>We help you get<br>financial assistance</span></div>
  <div class="feature" style="left:466px;top:136px"><svg width="76" height="76" viewBox="0 0 76 76"><circle cx="38" cy="38" r="36" fill="none" stroke="#fff" stroke-width="2"/><rect x="25" y="25" width="26" height="26" fill="none" stroke="#fff" stroke-width="3"/><path d="M30 37l7 7 14-16" fill="none" stroke="#fff" stroke-width="3"/></svg><span>We help you choose<br>the right plan</span></div>
  <div class="feature" style="left:766px;top:136px"><svg width="76" height="76" viewBox="0 0 76 76"><circle cx="38" cy="38" r="36" fill="none" stroke="#fff" stroke-width="2"/><circle cx="30" cy="30" r="5" fill="#fff"/><circle cx="46" cy="30" r="5" fill="#fff"/><path d="M22 50c0-8 4-12 8-12s8 4 8 12M38 50c0-8 4-12 8-12s8 4 8 12" fill="#fff"/></svg><span>We make sure you get<br>the BEST deal possible</span></div>
  <div class="feature" style="left:192px;top:262px"><svg width="76" height="76" viewBox="0 0 76 76"><circle cx="38" cy="38" r="36" fill="none" stroke="#fff" stroke-width="2"/><rect x="26" y="24" width="24" height="28" fill="none" stroke="#fff" stroke-width="3"/><path d="M31 32h14M31 38h14M31 44h9" stroke="#fff" stroke-width="2"/></svg><span>We help you enroll</span></div>
  <div class="feature" style="left:466px;top:262px"><svg width="76" height="76" viewBox="0 0 76 76"><circle cx="38" cy="38" r="36" fill="none" stroke="#fff" stroke-width="2"/><rect x="24" y="28" width="28" height="22" rx="2" fill="#fff"/><path d="M33 28v-4h10v4" fill="none" stroke="#fff" stroke-width="3"/><path d="M38 33v12M32 39h12" stroke="#7a6e62" stroke-width="3"/></svg><span>We navigate you<br>through health reform</span></div>
  <div class="feature" style="left:766px;top:262px"><svg width="76" height="76" viewBox="0 0 76 76"><circle cx="38" cy="38" r="36" fill="none" stroke="#fff" stroke-width="2"/><path d="M22 38a16 14 0 0 1 32 0z" fill="#fff"/><path d="M38 38v12a3 3 0 0 1-6 0" fill="none" stroke="#fff" stroke-width="2.5"/></svg><span>We're always<br>here to help</span></div>
  <div class="cta"><span class="btn" style="width:180px">Let Us Help You</span></div>
</section>

<section class="band premiums">
  <h2 class="section-title">Real Monthly Premiums, Real People</h2>
  <div class="person" style="left:182px;top:124px"><div class="portrait" role="img" aria-label="Portrait of a 27 year old man" style="background:linear-gradient(160deg,#e4d8cc,#a99683)"></div>Male, 27<br>$27.12</div>
  <div class="person" style="left:396px;top:124px"><div class="portrait" role="img" aria-label="Portrait of a 43 year old woman" style="background:linear-gradient(160deg,#c9a58a,#6f4e3a)"></div>Female, 43<br>$82.33</div>
  <div class="person" style="left:610px;top:124px"><div class="portrait" role="img" aria-label="Portrait of a 62 year old man" style="background:linear-gradient(160deg,#e6e6e6,#b8b0a6)"></div>Male, 62<br>$35.34</div>
  <div class="person" style="left:818px;top:124px"><div class="portrait" role="img" aria-label="Single mother outdoors with her two children" style="background:linear-gradient(160deg,#b7d39a,#6f9a5a)"></div>Single Mom, 2 Kids<br>$37.76</div>
  <div class="person" style="left:182px;top:376px"><div class="portrait" role="img" aria-label="Family of four smiling together" style="background:linear-gradient(160deg,#f0d7b8,#c98f6a)"></div>Family Of 4<br>$132.44</div>
  <div class="person" style="left:396px;top:376px"><div class="portrait" role="img" aria-label="Married couple hugging outdoors" style="background:linear-gradient(160deg,#e8dbc6,#a88b6d)"></div>Married Couple<br>$89.12</div>
  <div class="person" style="left:610px;top:376px"><div class="portrait" role="img" aria-label="Family of three on a sunny day" style="background:linear-gradient(160deg,#bfd6ea,#7c9bbd)"></div>Family Of 3<br>$56.12</div>
  <div class="person" style="left:818px;top:376px"><div class="portrait" role="img" aria-label="Portrait of a 57 year old woman" style="background:linear-gradient(160deg,#eee2d6,#c2a38a)"></div>Female, 57<br>$77.67</div>
  <div class="count">Over 1,395,929 People Have Enrolled in Sheltered Pacifica.</div>
  <div class="cta"><span class="btn" style="width:216px">Get Your Quote Now</span></div>
</section>

<section class="band testimonials">
  <h2 class="section-title">Testimonials</h2>
  <svg class="slide-arrow" style="left:136px;top:168px" width="18" height="40" viewBox="0 0 18 40"><path d="M16 2L3 20l13 18" fill="none" stroke="#bfe6e3" stroke-width="2"/></svg>
  <svg class="slide-arrow" style="left:1046px;top:168px" width="18" height="40" viewBox="0 0 18 40"><path d="M2 2l13 18L2 38" fill="none" stroke="#bfe6e3" stroke-width="2"/></svg>
  <div class="portrait" role="img" aria-label="Smiling blonde woman, the testimonial author"></div>
  <div class="q" style="left:457px;top:106px">&ldquo;</div>
  <blockquote>want to thank you so much for making time to chat with me and help me figure out my health insurance. You definitely saved me from a complete meltdown or two! I would highly recommend you to anyone that asked.</blockquote>
  <div class="q" style="left:944px;top:192px">&rdquo;</div>
  <div class="who">Lena M. &nbsp;&nbsp;|&nbsp;&nbsp; Rocklin, CA</div>
</section>

<section class="band choices">
  <h2 class="section-title">Choices For Affordable Health Coverage</h2>
  <svg class="slide-arrow" style="left:172px;top:158px" width="12" height="24" viewBox="0 0 12 24"><path d="M10 2L2 12l8 10" fill="none" stroke="#bbb" stroke-width="2"/></svg>
  <svg class="slide-arrow" style="left:1014px;top:158px" width="12" height="24" viewBox="0 0 12 24"><path d="M2 2l8 10-8 10" fill="none" stroke="#bbb" stroke-width="2"/></svg>
  <div class="partner" style="left:201px">Arborline</div>
  <div class="partner" style="left:364px">Veradyn</div>
  <div class="partner" style="left:528px">Kestrel</div>
  <div class="partner" style="left:691px">Nuvora</div>
  <div class="partner" style="left:855px">Calderis</div>
</section>

<footer class="band site-footer">
  <h3 class="foot-title" style="left:172px">Contact us</h3>
  <ul class="foot-list" style="left:172px;top:80px"><li>Phone : 800-555-0147</li><li>Time : M-F | 8am-5pm</li><li>Email : help@brightpath.example</li></ul>
  <div class="follow"><span class="label">Follow us :</span><span class="social"></span><span class="social"></span></div>
  <h3 class="foot-title" style="left:412px">Quick Links</h3>
  <ul class="foot-list" style="left:412px;top:78px;line-height:22.5px;font-size:10.5px"><li>Eligibility Chart</li><li>Standard Benefits</li><li>Enhanced Benefits</li><li>Household Income Worksheet</li><li>Agent Delegation</li><li>Service Appointment Authorization</li><li>Appeals Process</li></ul>
  <h3 class="foot-title" style="left:653px">Quick Links</h3>
  <div class="news" style="top:82px"><span class="date">SEP<br>01<br>2014</span><span><b>Consequat id duo, cu aeterno</b><br>Consequat id duo, cu aeterno inductum his. Ornatus docendi instructior...</span></div>
  <div class="news" style="top:162px"><span class="date">SEP<br>01<br>2014</span><span><b>Consequat id duo, cu aeterno</b><br>Consequat id duo, cu aeterno inductum his. Ornatus docendi instructior...</span></div>
</footer>

<div class="chat">
  <div class="close">&times;</div>
  <div class="brandline"><span class="dot"></span>Wellmora</div>
  <div class="input">Type here and press enter..</div>
</div>

<div class="band legal">
  Sheltered Pacifica&trade; and the Sheltered Pacifica Logo are registered trademarks or service marks of Sheltered Pacifica, in the United States. This website is owned and maintained by Sunward Crest Insurance Services, Inc., which is solely responsible for its content. This site is not maintained by or is listed with Sheltered Pacifica, and Sheltered Pacifica bears no responsibility for its content. The e-mail addresses and telephone numbers that appear throughout this site belong to Sunward Crest Insurance Services, Inc. and cannot be used to contact Sheltered Pacifica.
  <div class="code">CB</div>
</div>

</body>
</html>
```